Billboard

we want our Hop & Skip logo really big, we need this to stand out

Use a really bold font for the wording as it's on a billboard on the highway

Hop & Skip Logo
perhaps on left hand side really large then have a slanting line and a different colour background for the other side.

Wording BELOW-bold

TOUR NOW

hopandskip.edu.au

Use one image,
I have attached other designs we have been using for our campaign so a similar look would be great.
specs- 1224 W × 324 H px JPEG

Target Market(s)
families

Industry/Entity Type
childcare

Target Market(s)

families

Industry/Entity Type

childcare

Requirements
Must have
• bold font and big logo

```html
<!DOCTYPE html>
<html lang="en">
<head>
<meta charset="utf-8">
<title>Hop &amp; Skip – Tour Now Billboard</title>
<link href="https://fonts.googleapis.com/css2?family=Montserrat:wght@800;900&display=swap" rel="stylesheet">
<style>
  :root {
    --sky-blue: #00aeef;
    --banner-red: #e83c38;
    --sun-yellow: #fff200;
    --paper-white: #ffffff;
    --ink-black: #111111;
    --backdrop: #ececec;
    --photo-warm: #d9a877;
    --photo-deep: #8a6a45;
    --photo-light: #f1d9b5;
  }
  * { margin: 0; padding: 0; box-sizing: border-box; }
  html, body {
    width: 1200px;
    height: 1131px;
    overflow: hidden;
    background: var(--backdrop);
  }
  .billboard {
    position: absolute;
    left: 20px;
    top: 412px;
    width: 1160px;
    height: 306px;
    box-shadow: 0 6px 14px rgba(0,0,0,0.35);
    overflow: hidden;
    font-family: "Montserrat", "Arial Black", sans-serif;
  }
  .billboard__shapes {
    position: absolute;
    inset: 0;
  }
  .brand-name {
    position: absolute;
    left: 0;
    top: 0;
    width: 307px;
    height: 306px;
    display: flex;
    align-items: center;
    justify-content: center;
    text-align: center;
    color: var(--paper-white);
    font-weight: 900;
    font-size: 70px;
    line-height: 0.98;
    letter-spacing: -1px;
  }
  .headline {
    position: absolute;
    left: 350px;
    top: 28px;
    color: var(--sun-yellow);
    font-weight: 900;
    font-size: 111px;
    line-height: 103px;
    letter-spacing: -1px;
  }
  .headline span { display: block; }
  .headline .headline__now { padding-left: 16px; }
  .web-address {
    position: absolute;
    left: 385px;
    top: 247px;
    width: 545px;
    height: 39px;
    display: flex;
    align-items: center;
    justify-content: center;
    color: var(--ink-black);
    font-weight: 800;
    font-size: 25px;
    letter-spacing: 1px;
  }
</style>
</head>
<body>
  <section class="billboard">
    <svg class="billboard__shapes" width="1160" height="306" viewBox="0 0 1160 306" xmlns="http://www.w3.org/2000/svg">
      <defs>
        <linearGradient id="photoTone" x1="0" y1="0" x2="1" y2="1">
          <stop offset="0" stop-color="var(--photo-deep)"/>
          <stop offset="0.45" stop-color="var(--photo-warm)"/>
          <stop offset="1" stop-color="var(--photo-light)"/>
        </linearGradient>
      </defs>
      <rect class="panel-brand" x="0" y="0" width="307" height="306" fill="var(--sky-blue)"/>
      <rect class="panel-divider" x="307" y="0" width="6" height="306" fill="var(--paper-white)"/>
      <rect class="panel-message" x="313" y="0" width="847" height="306" fill="var(--banner-red)"/>
      <polygon class="photo-frame" points="820,0 1160,0 1160,306 908,306 730,87" fill="var(--paper-white)"/>
      <polygon class="photo-area" role="img" aria-label="Photo of smiling toddlers in blue sun hats playing with sand toys and a bucket in a kindergarten sandpit" points="833,0 1160,0 1160,306 920,306 743,87" fill="url(#photoTone)"/>
      <polygon class="web-address__pill" points="396,247 930,247 919,286 385,286" fill="var(--paper-white)"/>
    </svg>

    <div class="brand-name">Hop &amp;<br>Skip</div>

    <h1 class="headline">
      <span class="headline__tour">TOUR</span>
      <span class="headline__now">NOW</span>
    </h1>

    <p class="web-address">WWW.HOPANDSKIP.EDU.AU</p>
  </section>
</body>
</html>
```